We need a striking new book cover for a new book.

This book presents a modern concept based on the latest discoveries in the field of molecular genetics and nuclear physics. It helps us to understand the direction in which the universe, the world and each of us as individuals could be heading given the impact of laws of physics and evolution.

Book Title: The Quiet Lantern Doctrine
Author: Radosław Wenta

The text to go on the front cover is as follows :

The Quiet Lantern Doctrine
Radosław Wenta
is a scientist, author, publisher and a member of ORVIK

The photograph of the author uploaded should go on the back cover.
The text to go on the back cover is as follows:

This book presents a modern concept based on the latest discoveries in the field of molecular genetics and nuclear physics. It helps us to understand the direction in which the universe, the world, and each of us as individuals could be heading, given the impact of the laws of physics, and evolution. Entropy (law of physics) implies increasing chaos and that our universe inclines towards ever greater disorder.
Evolution means that everything evolves into more and more complex structures.

When entropy and evolution work together they create further sophistication in life on Earth. Chaos-driven evolution has not only created gravity, i.e. cosmic objects such as stars and planets, but it is also the driving force behind the changes on Earth now, and governs not just the universe and our planet, but also our lives and even our bodies.

Evolution sets goals while entropy is the driving force. Societies are becoming more open and progressive. Our freedom is increasing. Evolution keeps bringing more diversification. Scientific progress is accelerating and reducing the need for religions. We are seeing progress in social awareness and morality.
There are constant transfers of energy powering all changes in the micro- and macro- scale, as well as the everyday life of each of us.
Our world is at a major junction and our choices will benefit or taint future generations.

Radosław Wenta, is a scientist, author, publisher and a member of ORVIK.
He studied at both Brenmoor University and Tallowfield University. Having completed his studies in Biological Chemistry, he then further broadened his scientific experience whilst working in digital molecular genetics in the UK. In Poland he has conducted extensive research in the field of auto-immune diseases. He also holds an MBA. He is the author of a number of scientific works and guide books.

```html
<!DOCTYPE html>
<html lang="en">
<head>
<meta charset="utf-8">
<title>The Quiet Lantern Doctrine — Book Cover</title>
<link href="https://fonts.googleapis.com/css2?family=Bebas+Neue&family=Montserrat:wght@600&family=Oswald:wght@600&family=Roboto:wght@400&display=swap" rel="stylesheet">
<style>
  :root {
    --page-bg: #f1f1f1;
    --cover-dark: #0b0e14;
    --cover-deep: #05070b;
    --text-light: #e4e8ee;
    --white: #ffffff;
    --blue-deep: #2d4fa8;
    --blue-mid: #3f7fd0;
    --blue-light: #6fc6ee;
    --cyan: #4fd0ee;
    --band-start: #2f6fb7;
    --band-end: #66b9e8;
  }
  * { box-sizing: border-box; margin: 0; padding: 0; }
  html, body { width: 1200px; height: 1000px; overflow: hidden; }
  body { background: var(--page-bg); position: relative; font-family: "Roboto", Arial, sans-serif; }

  /* Back cover */
  .back-cover {
    position: absolute; left: 73px; top: 142px; width: 484px; height: 743px;
    background: linear-gradient(180deg, #0d1119 0%, var(--cover-dark) 60%, #10151f 100%);
    color: var(--text-light);
  }
  .back-title {
    position: absolute; left: 0; right: 0; top: 42px; text-align: center;
    font-family: "Bebas Neue", "Oswald", sans-serif; font-size: 44px; letter-spacing: 0.5px;
    color: var(--white); line-height: 1;
  }
  .back-title .accent {
    background: linear-gradient(90deg, var(--blue-deep), var(--blue-light));
    -webkit-background-clip: text; background-clip: text; color: transparent;
  }
  .back-content {
    position: absolute; left: 44px; top: 95px; width: 396px;
    display: flex; flex-direction: column;
  }
  .back-copy {
    font-size: 10.9px; line-height: 13.2px; text-align: justify;
  }
  .back-copy p { margin-bottom: 12px; }
  .back-copy .highlight {
    color: var(--cyan); font-size: 16px; line-height: 20px; text-align: center;
    margin: 18px 0 16px;
  }
  .author-row {
    display: flex; gap: 22px; align-items: flex-start; margin-top: 12px;
  }
  .author-photo {
    flex: 0 0 89px; height: 126px;
    border: 2px solid var(--cyan);
    background: linear-gradient(180deg, #6d5c4a 0%, #4a4038 45%, #1d1d22 100%);
  }
  .author-bio {
    flex: 1; font-size: 10.9px; line-height: 13.2px; text-align: justify;
  }

  /* Spine */
  .spine {
    position: absolute; left: 574px; top: 142px; width: 63px; height: 743px;
    background: linear-gradient(180deg, #151b26, var(--cover-deep));
    overflow: hidden;
  }
  .spine-band { position: absolute; left: 0; top: 0; width: 63px; height: 743px; }
  .spine-title, .spine-author {
    position: absolute; left: 50%; white-space: nowrap;
    transform-origin: 0 0; transform: rotate(90deg);
  }
  .spine-title {
    top: 40px; margin-left: 18px;
    font-family: "Bebas Neue", "Oswald", sans-serif; font-size: 37px; color: var(--white); line-height: 1;
  }
  .spine-title .accent {
    background: linear-gradient(90deg, var(--blue-deep), var(--blue-light));
    -webkit-background-clip: text; background-clip: text; color: transparent;
  }
  .spine-author {
    top: 548px; margin-left: 9px;
    font-family: "Montserrat", Arial, sans-serif; font-weight: 600; font-size: 15px;
    letter-spacing: 2px; color: var(--white);
  }

  /* Front cover */
  .front-cover {
    position: absolute; left: 653px; top: 142px; width: 482px; height: 743px;
    background: var(--cover-deep); overflow: hidden;
  }
  .front-photo {
    position: absolute; inset: 0;
    background:
      radial-gradient(ellipse 160px 120px at 55% 10%, rgba(255,214,140,0.95), rgba(244,132,52,0.7) 45%, transparent 100%),
      linear-gradient(180deg, #8aa3bd 0%, #d88a46 22%, #6e7f95 38%, #9aa7b6 55%, #3b4654 72%, var(--cover-deep) 82%);
  }
  .front-title {
    position: absolute; left: 0; right: 0; top: 432px; text-align: center;
    font-family: "Bebas Neue", "Oswald", sans-serif; color: var(--white); line-height: 0.9;
  }
  .front-title .line-small { display: block; font-size: 44px; letter-spacing: 9px; }
  .front-title .line-accent {
    display: block; font-size: 104px;
    background: linear-gradient(90deg, var(--blue-deep), var(--blue-mid) 55%, var(--blue-light));
    -webkit-background-clip: text; background-clip: text; color: transparent;
  }
  .front-title .line-large { display: block; font-size: 132px; }
  .author-band {
    position: absolute; left: 0; right: 0; bottom: 0; height: 73px;
    background: linear-gradient(90deg, var(--band-start), var(--band-end));
    text-align: center; color: var(--white);
  }
  .author-band .author-name {
    font-family: "Montserrat", Arial, sans-serif; font-weight: 600;
    font-size: 31px; letter-spacing: 6px; line-height: 1; padding-top: 9px;
  }
  .author-band .author-tagline {
    font-family: "Oswald", Arial, sans-serif; font-weight: 600;
    font-size: 12.5px; letter-spacing: 1.3px; margin-top: 5px;
  }
</style>
</head>
<body>

  <section class="back-cover">
    <h2 class="back-title">The Quiet <span class="accent">Lantern</span> Doctrine</h2>
    <div class="back-content">
      <div class="back-copy">
        <p>This book presents a modern concept based on the latest discoveries in the field of molecular genetics and nuclear physics. It helps us to understand the direction in which the universe, the world, and each of us as individuals could be heading, given the impact of the laws of physics, and evolution. Entropy (law of physics) implies increasing chaos and that our universe inclines towards ever greater disorder.</p>
        <p class="highlight">Evolution means that everything evolves into more and more complex structures.</p>
        <p>When entropy and evolution work together they create further sophistication in life on Earth. Chaos-driven evolution has not only created gravity, i.e. cosmic objects such as stars and planets, but it is also the driving force behind the changes on Earth now, and governs not just the universe and our planet, but also our lives and even our bodies.</p>
        <p>Evolution sets goals while entropy is the driving force. Societies are becoming more open and progressive. Our freedom is increasing. Evolution keeps bringing more diversification. Scientific progress is accelerating and reducing the need for religions. We are seeing progress in social awareness and morality.</p>
        <p>There are constant transfers of energy powering all changes in the micro- and macro- scale, as well as the everyday life of each of us.</p>
        <p>Our world is at a major junction and our choices will benefit or taint future generations.</p>
      </div>
      <div class="author-row">
        <div class="author-photo" role="img" aria-label="Portrait photograph of the author"></div>
        <p class="author-bio">Radosław Wenta, is a scientist, author, publisher and a member of ORVIK.<br>He studied at both Brenmoor University and Tallowfield University. Having completed his studies in Biological Chemistry, he then further broadened his scientific experience whilst working in digital molecular genetics in the UK. In Poland he has conducted extensive research in the field of auto-immune diseases. He also holds an MBA. He is the author of a number of scientific works and guide books.</p>
      </div>
    </div>
  </section>

  <section class="spine">
    <svg class="spine-band" viewBox="0 0 63 743" aria-hidden="true">
      <defs>
        <linearGradient id="spineBlue" x1="0" y1="0" x2="1" y2="0">
          <stop offset="0" stop-color="#2f6fb7"/>
          <stop offset="1" stop-color="#4c96d6"/>
        </linearGradient>
      </defs>
      <polygon points="0,475 63,505 63,743 0,743" fill="url(#spineBlue)"/>
    </svg>
    <div class="spine-title">The Quiet <span class="accent">Lantern</span> Doctrine</div>
    <div class="spine-author">RADOSŁAW WENTA</div>
  </section>

  <section class="front-cover">
    <div class="front-photo" role="img" aria-label="Photograph of a businessman with a briefcase climbing a long staircase toward a sunlit city skyline at dawn"></div>
    <h1 class="front-title">
      <span class="line-small">The Quiet</span>
      <span class="line-accent">Lantern</span>
      <span class="line-large">Doctrine</span>
    </h1>
    <div class="author-band">
      <div class="author-name">RADOSŁAW WENTA</div>
      <div class="author-tagline">SCIENTIST, AUTHOR, PUBLISHER AND A MEMBER OF ORVIK</div>
    </div>
  </section>

</body>
</html>
```